Harbor Lane PEO - Web Build for Professional Employment Organization

We need a website built for our new PEO (professional employment organization). This company will offer third party Human Resource services to companies who are looking to outsource:<br/>Recruiting<br/>Administrative Onboarding<br/>New hire training, ongoing training and development<br/>Payroll/compensation processing/services<br/>Employee Relations<br/>Unemployment Claim Facilitation<br/>Benefits Plans and Administration<br/><br/>I have attached the logo below. Please use that as a reference and color match as best as possible. <br/><br/>Here are some of the competitor's websites:<br/>https://www.workvantrix.com/ <br/>https://www.staffmerola.com/<br/>https://www.staffmerola.com/<br/>https://www.qlr.com/<br/>https://www.hirebendora.com/<br/>https://corvalpeo.com/contact-corval/<br/><br/>

Target Market(s)

Startups and mid-sized businesses

Number of Pages Required

5+ page

Font styles to use
Sans Serif

Colors
0592cd

Requirements
Must have
• Features Pages
• SEO driven keyword rich content
• Strong focus on our ability to provide unemployment claim facilitation services as well as mandatory training/certification fulfillment
Nice to have
• I'd like to see one mockup with a Live Chat version if possible. In theory, the Live Chat messages would go directly to our front desk person.

```html
<!DOCTYPE html>
<html lang="en">
<head>
<meta charset="utf-8">
<title>Harbor Lane PEO – Professional Employment Organisation</title>
<link href="https://fonts.googleapis.com/css2?family=Open+Sans:wght@400;600;700&family=Lato:wght@400;700&display=swap" rel="stylesheet">
<style>
:root{
  --navy:#1e2438;
  --teal:#1b9db0;
  --teal-light:#8fd3dc;
  --ink:#2b2b2b;
  --footer:#25272a;
  --white:#ffffff;
  --photo-a:#4e5c6e;
  --photo-b:#c9b59a;
}
*{margin:0;padding:0;box-sizing:border-box}
html,body{width:1200px;height:5309px;overflow:hidden}
body{position:relative;background:var(--white);font-family:"Open Sans",Arial,sans-serif;color:var(--ink)}
.abs{position:absolute}
a{color:inherit;text-decoration:none}

/* header */
.site-header{position:absolute;left:0;top:0;width:1200px;height:105px}
.nav-band{position:absolute;left:0;top:62px;width:1200px;height:40px;background:var(--teal)}
.brand-tab{position:absolute;left:0;top:0;width:362px;height:108px;background:var(--white);border-bottom-right-radius:30px;border:3px solid var(--teal);border-left:none;border-top:none}
.brand-name{position:absolute;left:48px;top:28px;font-family:"Lato",sans-serif;font-weight:700;font-size:34px;color:var(--navy);letter-spacing:1px}
.top-btn{position:absolute;top:10px;height:36px;background:var(--teal);color:var(--white);font-size:14px;line-height:36px;text-align:center;border-radius:4px}
.main-nav a{position:absolute;top:72px;font-size:14px;color:var(--white)}

/* hero */
.hero{position:absolute;left:0;top:102px;width:1200px;height:618px;background:var(--navy);overflow:hidden}
.hero-eyebrow{position:absolute;left:42px;top:148px;font-size:30px;font-weight:700;color:var(--teal)}
.hero-title{position:absolute;left:42px;top:196px;font-size:42px;font-weight:400;color:var(--white)}
.hero-copy{position:absolute;left:46px;top:264px;width:440px;font-size:20px;line-height:31.5px;color:var(--white)}
.btn{position:absolute;background:var(--teal);color:var(--white);font-size:19px;text-align:center;border-radius:4px}

/* services */
.service{position:absolute;width:262px;height:262px;border:2px solid var(--teal);background:var(--white)}
.service .ico{position:absolute;left:64px;top:42px;width:132px;height:132px}
.service p{position:absolute;left:0;bottom:10px;width:100%;text-align:center;font-size:19px;line-height:25px;color:var(--ink)}
.ico-line{fill:none;stroke:var(--white);stroke-width:3.5;stroke-linecap:round;stroke-linejoin:round}

/* about */
.about{position:absolute;left:0;top:1620px;width:1200px;height:568px;background:var(--navy)}
.about h2{position:absolute;left:720px;top:50px;width:420px;text-align:center;font-size:34px;font-weight:600;color:var(--white)}
.about p{position:absolute;left:690px;top:130px;width:480px;text-align:center;font-size:20px;line-height:31.5px;font-weight:600;color:var(--white)}

/* requirement */
.req-title{position:absolute;left:0;top:2386px;width:1200px;text-align:center;font-size:24px;font-weight:400;color:var(--teal)}
.req-shape{position:absolute;width:168px;height:168px}
.req-label{position:absolute;top:2656px;font-size:20px;color:var(--ink);display:flex;align-items:center;gap:10px}
.radio{width:24px;height:24px;border:2px solid #444;border-radius:50%}

/* how it works */
.how{position:absolute;left:0;top:2950px;width:1200px;height:494px;background:var(--navy);color:var(--white)}
.how h2{position:absolute;top:24px;width:1200px;text-align:center;font-size:25px;font-weight:400}
.step h3{font-family:"Lato",sans-serif;font-size:32px;letter-spacing:2px;font-weight:700}
.step p{font-size:16px;line-height:27px;margin-top:2px}
.step{position:absolute}

/* body copy */
.body-copy{position:absolute;left:112px;top:3516px;width:976px;text-align:center;font-size:21px;line-height:31.6px;letter-spacing:0.8px}

/* testimonial */
.testimonial{position:absolute;left:0;top:4190px;width:1200px;height:438px;background:var(--navy);color:var(--white)}
.quote-mark{position:absolute;font-size:90px;color:#7d8291;font-family:Georgia,serif;font-style:italic}
.quote-text{position:absolute;left:180px;top:60px;width:450px;text-align:center;font-size:17px;line-height:31px}
.quote-name{position:absolute;left:320px;top:312px;font-size:20px;color:var(--teal)}
.quote-role{position:absolute;left:320px;top:346px;font-size:16px;line-height:32px}

/* social */
.connect{position:absolute;left:98px;top:4648px;font-size:32px;font-weight:400;color:var(--teal);letter-spacing:2px}
.social{position:absolute;top:4708px;width:44px;height:44px;border-radius:50%;background:var(--teal)}

/* footer */
.site-footer{position:absolute;left:0;top:4785px;width:1200px;height:524px;background:var(--footer);color:var(--white)}
.site-footer h4{position:absolute;font-size:32px;font-weight:400;letter-spacing:2px}
.foot-list{position:absolute;font-size:21px;line-height:48px;letter-spacing:1.5px}
.foot-list a{display:block;text-decoration:underline}
.contact-info{position:absolute;left:92px;top:175px;font-size:21px;line-height:36px;letter-spacing:1.5px}
.rule{position:absolute;left:64px;top:431px;width:1000px;height:1px;background:#777}
.legal{position:absolute;left:0;width:1120px;text-align:center;font-size:10px;font-weight:700}
</style>
</head>
<body>

<svg class="abs" style="left:0;top:0" width="1200" height="5309" aria-hidden="true">
  <g fill="none" stroke="var(--teal-light)" stroke-width="6" stroke-dasharray="30 16">
    <path d="M355 720 C380 880 330 1080 0 1195"/>
    <path d="M1200 1470 C1090 1500 1010 1560 975 1625"/>
    <path d="M1045 2180 C1100 2240 1160 2260 1200 2275"/>
    <path d="M0 2420 C150 2280 420 2280 550 2370 C730 2510 780 2730 720 2950"/>
    <path d="M520 3444 C540 3620 560 3800 540 3950"/>
    <path d="M640 3930 C820 3970 1050 3900 1200 3810"/>
  </g>
</svg>

<header class="site-header">
  <div class="nav-band"></div>
  <div class="brand-tab"><span class="brand-name">Harbor Lane PEO</span></div>
  <a class="top-btn" style="left:848px;width:158px" href="#">LOGIN/SIGNUP</a>
  <a class="top-btn" style="left:1038px;width:100px" href="#">CONTACT US</a>
  <nav class="main-nav">
    <a style="left:491px" href="#">ABOUT</a>
    <a style="left:626px" href="#">RESOURCES</a>
    <a style="left:797px" href="#">CAREER</a>
    <a style="left:935px" href="#">SOLUTIONS</a>
    <a style="left:1106px" href="#">.NEWS</a>
  </nav>
</header>

<section class="hero">
  <svg class="abs" style="left:0;top:0" width="1200" height="618">
    <defs><linearGradient id="heroPhoto" x1="0" y1="0" x2="1" y2="1"><stop offset="0" stop-color="var(--photo-a)"/><stop offset="1" stop-color="var(--photo-b)"/></linearGradient></defs>
    <path d="M1200 0 L610 0 C470 40 430 230 520 380 C610 520 850 600 1200 618 Z" fill="var(--teal)"/>
    <path role="img" aria-label="Photo of two women working at a computer" d="M1200 0 L625 0 C495 45 455 230 540 370 C625 505 860 585 1200 600 Z" fill="url(#heroPhoto)"/>
  </svg>
  <div class="hero-eyebrow">HARBOR LANE</div>
  <h1 class="hero-title">Professional Employment Organisation</h1>
  <p class="hero-copy">Lorem ipsum dolor sit amet, consectetur adipiscing elit, sed do eiusmod tempor incididunt ut labore et dolore magna aliqua. Quis ipsum suspendisse ultrices gravida. Risus commodo viverra maecenas accumsan lacus vel facilisis.</p>
  <a class="btn" style="left:42px;top:482px;width:242px;height:60px;line-height:60px" href="#">EXPLORE SERVICES</a>
</section>

<!-- services -->
<div class="service" style="left:95px;top:864px">
  <svg class="ico" viewBox="0 0 132 132" role="img" aria-label="Recruiting signpost icon">
    <circle cx="66" cy="66" r="66" fill="var(--teal)"/>
    <g class="ico-line"><path d="M66 24 V108 M56 108 h20"/><path d="M40 36 h56 l8 9 -8 9 H40 l-8 -9 Z"/><path d="M40 62 h56 l8 9 -8 9 H40 l-8 -9 Z"/></g>
    <g fill="var(--white)" font-family="Open Sans,sans-serif" font-weight="700" font-size="13" text-anchor="middle"><text x="68" y="50">JOB</text><text x="68" y="76">JOB</text></g>
  </svg>
  <p>RECRUITING</p>
</div>
<div class="service" style="left:435px;top:864px">
  <svg class="ico" viewBox="0 0 132 132" role="img" aria-label="Onboarding icon with person and chat bubble">
    <circle cx="66" cy="66" r="66" fill="var(--teal)"/>
    <g class="ico-line"><circle cx="46" cy="62" r="10"/><path d="M28 100 c0 -16 8 -24 18 -24 s18 8 18 24"/><path d="M64 88 h36 l-6 14 H58 Z"/><circle cx="84" cy="42" r="18"/><path d="M72 56 l-6 10 10 -5"/><path d="M76 40 h16 M76 47 h10"/></g>
  </svg>
  <p>ADMINISTRATIVE<br>ONBOARDING</p>
</div>
<div class="service" style="left:776px;top:864px">
  <svg class="ico" viewBox="0 0 132 132" role="img" aria-label="Training icon with presentation board">
    <circle cx="66" cy="66" r="66" fill="var(--teal)"/>
    <g class="ico-line"><rect x="36" y="30" width="64" height="40" rx="2"/><path d="M50 60 l12 -10 10 6 16 -16"/><path d="M80 40 h8 v8"/><circle cx="46" cy="84" r="7"/><circle cx="66" cy="84" r="7"/><circle cx="86" cy="84" r="7"/><path d="M34 106 c0 -10 5 -14 12 -14 s12 4 12 14 M54 106 c0 -10 5 -14 12 -14 s12 4 12 14 M74 106 c0 -10 5 -14 12 -14 s12 4 12 14"/></g>
  </svg>
  <p>NEW HIRE TRAINING,<br>DEVELOPMENT</p>
</div>
<div class="service" style="left:95px;top:1190px">
  <svg class="ico" viewBox="0 0 132 132" role="img" aria-label="Payroll icon with banknote and coin">
    <circle cx="66" cy="66" r="66" fill="var(--teal)"/>
    <g class="ico-line"><rect x="34" y="34" width="70" height="50" rx="3"/><rect x="42" y="42" width="54" height="34" rx="2"/><path d="M54 56 h30 M58 64 h22"/><circle cx="44" cy="90" r="14"/><path d="M48 84 c-2 -2 -10 -2 -10 2 s10 2 10 7 -8 4 -10 1 M44 80 v4 M44 97 v3"/></g>
  </svg>
  <p>PAYROLL/COMPENSATION<br>PROCESSING/SERVICES</p>
</div>
<div class="service" style="left:435px;top:1190px">
  <svg class="ico" viewBox="0 0 132 132" role="img" aria-label="Employee relations icon with people">
    <circle cx="66" cy="66" r="66" fill="var(--teal)"/>
    <g class="ico-line"><circle cx="76" cy="40" r="11"/><path d="M56 104 V74 c0 -12 8 -18 20 -18 s20 6 20 18 v30"/><path d="M76 56 v48"/><circle cx="44" cy="64" r="7"/><path d="M32 104 V84 c0 -6 5 -10 12 -10"/><rect x="36" y="88" width="20" height="14" rx="2"/></g>
  </svg>
  <p>EMPLOYEE RELATIONS&lt;</p>
</div>
<div class="service" style="left:776px;top:1190px">
  <svg class="ico" viewBox="0 0 132 132" role="img" aria-label="Claim form icon with checklist and pen">
    <circle cx="66" cy="66" r="66" fill="var(--teal)"/>
    <g class="ico-line"><rect x="34" y="28" width="52" height="76" rx="3"/><rect x="42" y="40" width="8" height="8"/><rect x="42" y="58" width="8" height="8"/><rect x="42" y="76" width="8" height="8"/><path d="M56 44 h20 M56 62 h20 M56 80 h20"/><path d="M94 36 v56 l5 10 5 -10 V36 Z"/></g>
  </svg>
  <p>UNEMPLOYMENT<br>CLAIM FACILITATION</p>
</div>

<section class="about">
  <h2>ABOUT US</h2>
  <p>Lorem ipsum dolor sit amet, consectetur adipiscing elit. Proin fringilla nibh nec laoreet molestie. Nunc efficitur massa orci, ut maximus nibh hendrerit in. Sed non dui ante. Quisque varius convallis enim sed ultricies. Interdum et malesuada fames ac ante ipsum primis in faucibus. Suspendisse potenti. Vestibulum sit amet mollis elit. Curabitur gravida laoreet enim, vitae ultricies lectus placerat sit amet. Mauris in convallis turpis, quis auctor tellus. Fusce sapien mi, tempor</p>
</section>
<svg class="abs" style="left:0;top:1546px" width="660" height="700">
  <defs><linearGradient id="aboutPhoto" x1="0" y1="0" x2="1" y2="1"><stop offset="0" stop-color="#d9d6cf"/><stop offset="1" stop-color="#6b7a8c"/></linearGradient></defs>
  <path d="M0 0 C220 0 520 40 630 140 C700 230 640 430 470 560 C320 680 130 700 0 660 Z" fill="var(--teal)"/>
  <path role="img" aria-label="Photo of a team reviewing plans around a desk" d="M0 0 C220 -5 505 45 612 145 C680 235 620 425 458 548 C315 662 130 685 0 646 Z" fill="url(#aboutPhoto)"/>
</svg>

<h2 class="req-title">PLEASE SELECT YOUR REQUIREMENT BELOW</h2>
<svg class="req-shape" style="left:206px;top:2470px" viewBox="0 0 168 168" role="img" aria-label="Single employee icon">
  <rect x="30" y="30" width="108" height="108" rx="34" transform="rotate(45 84 84)" fill="var(--teal)"/>
  <rect x="24" y="24" width="120" height="120" rx="38" transform="rotate(45 84 84)" fill="none" stroke="var(--teal)" stroke-width="2"/>
  <g fill="none" stroke="var(--navy)" stroke-width="3.5" stroke-linejoin="round"><circle cx="84" cy="68" r="14"/><path d="M60 116 V100 c0 -10 10 -16 24 -16 s24 6 24 16 v16 Z"/><path d="M84 86 v28"/></g>
</svg>
<svg class="req-shape" style="left:513px;top:2470px" viewBox="0 0 168 168" role="img" aria-label="Small team icon">
  <rect x="30" y="30" width="108" height="108" rx="34" transform="rotate(45 84 84)" fill="var(--teal)"/>
  <rect x="24" y="24" width="120" height="120" rx="38" transform="rotate(45 84 84)" fill="none" stroke="var(--teal)" stroke-width="2"/>
  <g fill="none" stroke="var(--navy)" stroke-width="3.5" stroke-linejoin="round"><circle cx="84" cy="66" r="10"/><circle cx="62" cy="76" r="9"/><circle cx="106" cy="76" r="9"/><path d="M66 114 V96 c0 -8 8 -14 18 -14 s18 6 18 14 v18"/><path d="M48 114 V102 c0 -7 6 -12 14 -12 M120 114 V102 c0 -7 -6 -12 -14 -12"/></g>
</svg>
<svg class="req-shape" style="left:821px;top:2470px" viewBox="0 0 168 168" role="img" aria-label="Large team icon">
  <rect x="30" y="30" width="108" height="108" rx="34" transform="rotate(45 84 84)" fill="var(--teal)"/>
  <rect x="24" y="24" width="120" height="120" rx="38" transform="rotate(45 84 84)" fill="none" stroke="var(--teal)" stroke-width="2"/>
  <g fill="none" stroke="var(--navy)" stroke-width="3.5" stroke-linejoin="round"><circle cx="66" cy="60" r="8"/><circle cx="102" cy="60" r="8"/><circle cx="84" cy="86" r="9"/><path d="M52 84 c0 -8 6 -12 14 -12 s14 4 14 12 M88 84 c0 -8 6 -12 14 -12 s14 4 14 12"/><path d="M66 118 V106 c0 -6 8 -10 18 -10 s18 4 18 10 v12"/><circle cx="56" cy="96" r="7"/><circle cx="112" cy="96" r="7"/></g>
</svg>
<label class="req-label" style="left:188px"><span class="radio"></span>0-50 EMPLOYEES</label>
<label class="req-label" style="left:478px"><span class="radio"></span>50-100 EMPLOYEES</label>
<label class="req-label" style="left:798px"><span class="radio"></span>&gt;100 EMPLOYEES</label>
<a class="btn" style="left:452px;top:2770px;width:296px;height:58px;line-height:58px" href="#">GET A QUOTATION</a>

<section class="how">
  <h2>HOW IT WORK'S ?</h2>
  <div class="step" style="left:143px;top:142px">
    <svg class="abs" style="left:4px;top:-4px" width="66" height="62" aria-hidden="true"><g fill="none" stroke="var(--teal)" stroke-width="3"><circle cx="16" cy="12" r="8"/><circle cx="50" cy="12" r="8"/><path d="M4 60 V28 h24 v32 M38 60 V28 h24 v32"/></g></svg>
    <h3 style="margin-left:82px;margin-top:14px">SEEK.</h3>
    <p style="width:220px">In finibus dolor et ipsum eleifend pulvinar. Pellentesque fermentum leo massa, vitae suscipit augue</p>
  </div>
  <div class="step" style="left:490px;top:128px">
    <svg class="abs" style="left:12px;top:-4px" width="62" height="72" aria-hidden="true"><g fill="none" stroke="var(--teal)" stroke-width="3"><circle cx="12" cy="10" r="6"/><circle cx="31" cy="10" r="6"/><circle cx="50" cy="10" r="6"/><path d="M4 70 L12 22 L20 70 M23 70 L31 22 L39 70 M42 70 L50 22 L58 70"/></g></svg>
    <h3 style="margin-left:84px;margin-top:30px">SOLVE.</h3>
    <p style="width:200px">vPhasellus ac feugiat sem, a vehicula velit. Duis id viverra erat. Etiam vitae nisl eget lorem porta viverra ac vel lacus. Suspendisse</p>
  </div>
  <div class="step" style="left:848px;top:124px">
    <svg class="abs" style="left:10px;top:-6px" width="66" height="66" aria-hidden="true"><g fill="none" stroke="var(--teal)" stroke-width="3"><circle cx="33" cy="12" r="9"/><circle cx="12" cy="44" r="7"/><circle cx="54" cy="44" r="7"/><path d="M2 64 a10 10 0 0 1 20 0 M44 64 a10 10 0 0 1 20 0 M24 44 h18"/></g></svg>
    <h3 style="margin-left:84px;margin-top:30px">SHARE.</h3>
    <p style="width:220px">Vivamus venenatis, eros a varius dapibus, nisl erat congue ante, et fringilla dolor nulla eget quam. Mauris at enim fringilla, ultrices enim</p>
  </div>
</section>

<p class="body-copy">Phasellus ac feugiat sem, a vehicula velit. Duis id viverra erat. Etiam vitae nisl eget lorem porta viverra ac vel lacus. Suspendisse potenti. Etiam malesuada efficitur dui eu aliquet. Morbi molestie mollis nunc vitae tincidunt. Mauris at orci lectus. Integer eleifend tempor odio at efficitur. Aliquam sollicitudin at diam at sodales. Suspendisse tempus porttitor augue sit amet porttitor. Cras sit amet gravida massa. Suspendisse at felis nisi. Ut et ante hendrerit, vulputate tortor non, vestibulum dui. Mauris risus risus, vestibulum rutrum nisl nec, semper placerat sapien.Phasellus ac feugiat sem, a vehicula velit. Duis id viverra erat. Etiam vitae nisl eget lorem porta viverra ac vel lacus. Suspendisse potenti. Etiam malesuada efficitur dui eu aliquet. Morbi molestie mollis nunc vitae tincidunt. Mauris at orci lectus. Integer eleifend tempor odio at efficitur. Aliquam sollicitudin at diam at sodales. Suspendisse tempus porttitor augue sit amet porttitor. Cras sit amet gravida massa. Suspendisse at felis nisi. Ut et ante hendrerit, vulputate tortor non, vestibulum dui. Mauris risus risus, vestibulum rutrum nisl nec, semper placerat sapien.</p>
<a class="btn" style="left:452px;top:3990px;width:296px;height:58px;line-height:58px" href="#">CONTACT US</a>

<section class="testimonial">
  <span class="quote-mark" style="left:64px;top:20px">&ldquo;</span>
  <span class="quote-mark" style="left:620px;top:230px">&rdquo;</span>
  <p class="quote-text">Lorem ipsum dolor sit amet, consectetur adipiscing elit, sed do eiusmod tempor incididunt ut labore et dolore magna aliqua. Quis ipsum suspendisse ultrices gravida. Risus commodo viverra maecenas accumsan lacus vel facilisis.</p>
  <div class="quote-name">-DEAN MARLOW</div>
  <div class="quote-role">NATIONAL SALES MANAGER<br>Kestrel Ridge LIMITED</div>
</section>
<svg class="abs" style="left:700px;top:4140px" width="500" height="470">
  <circle cx="322" cy="232" r="226" fill="var(--teal)"/>
  <circle role="img" aria-label="Portrait photo of the national sales manager" cx="322" cy="232" r="216" fill="#c8c9cc"/>
</svg>

<h3 class="connect">Get connected with us:</h3>
<span class="social" style="left:100px" role="img" aria-label="Social link one"></span>
<span class="social" style="left:195px" role="img" aria-label="Social link two"></span>
<span class="social" style="left:291px" role="img" aria-label="Social link three"></span>
<span class="social" style="left:388px" role="img" aria-label="Social link four"></span>
<span class="social" style="left:484px" role="img" aria-label="Social link five"></span>

<footer class="site-footer">
  <h4 style="left:92px;top:96px">Contact us:</h4>
  <h4 style="left:505px;top:96px">Quick links</h4>
  <h4 style="left:860px;top:82px">Our company</h4>
  <div class="contact-info">phone:<br>+91 9000 555 210<br><br>email:<br>contact@harborlanepeo<br>.com</div>
  <div class="foot-list" style="left:506px;top:166px"><a href="#">about</a><a href="#">resources</a><a href="#">career</a><a href="#">solutions</a><a href="#">login/signup</a></div>
  <div class="foot-list" style="left:860px;top:166px"><a href="#">About us</a><a href="#">Corporate Citizenship</a><a href="#">Investor relations</a><a href="#">News</a></div>
  <div class="rule"></div>
  <p class="legal" style="top:456px">© Copyright 2020. All rights reserved. Harbor Lane Professionals Limited</p>
  <p class="legal" style="top:495px">Privacy Policy | Our Code | Contact Us &nbsp;Designed by Northwick Studio Pvt Ltd</p>
</footer>

</body>
</html>
```